Business Card for Bramble Gear

Target Market(s)

Mining, fleet, 4wd industry

Industry/Entity Type

Business

Requirements
Must have
• Front of card
Logo of Bramble Gear, the Nut preferrably top right corner and wording which says
"The Classic Kordo Bolt Products along bottom right hand corner
Use of the orange logo.
Back of card down left side to include (bullet points )
. Canvas Seat Covers
. Hi - Vis Flags
. Canvas or PVC designs by request.
back of card down right side
Danielle Rowbeck
Ph 02 49315728
E ; admin@bramblegear.com.au
W: www.bramblegear.com.au
Nice to have
• other designs can also be submitted as we require additional cards.

```html
<!DOCTYPE html>
<html lang="en">
<head>
<meta charset="utf-8">
<title>Bramble Gear – Business Card</title>
<link rel="stylesheet" href="https://fonts.googleapis.com/css2?family=Arimo:ital,wght@0,400;0,700;1,400&family=Open+Sans:wght@400&display=swap">
<style>
  :root {
    --stage: #5b5b5b;
    --paper: #ffffff;
    --brand-orange: #f39322;
    --brand-grey: #7f8184;
    --tagline-grey: #808285;
    --nut-dark: #8e2f2a;
    --nut-light: #d8a58a;
  }
  * { margin: 0; padding: 0; box-sizing: border-box; }
  html, body { width: 1020px; height: 1200px; overflow: hidden; }
  body {
    position: relative;
    background: var(--stage);
    font-family: "Arimo", Arial, sans-serif;
  }
  .card {
    position: absolute;
    left: 37px;
    width: 945px;
    height: 565px;
  }
  .card--front { top: 28px; background: var(--paper); }
  .card--back { top: 607px; height: 564px; background: var(--brand-orange); }

  .mascot {
    position: absolute;
    left: 617px; top: 54px;
    width: 234px; height: 232px;
    border-radius: 50%;
    background: radial-gradient(circle at 45% 45%, var(--nut-light), var(--nut-dark) 75%);
  }
  .tagline {
    position: absolute;
    right: 64px; top: 311px;
    font-style: italic;
    font-size: 26px;
    color: var(--tagline-grey);
  }
  .wordmark {
    position: absolute;
    left: 65px; top: 390px;
    font-weight: 700;
    font-size: 112px;
    line-height: 1;
    letter-spacing: -1px;
    color: var(--brand-grey);
    white-space: nowrap;
  }
  .card--back .wordmark { top: 56px; color: var(--paper); }

  .services {
    position: absolute;
    left: 61px; top: 414px;
    list-style: none;
    font-family: "Open Sans", Arial, sans-serif;
    font-size: 22px;
    line-height: 31px;
    color: var(--paper);
  }
  .services li::before {
    content: "";
    display: inline-block;
    width: 12px; height: 12px;
    margin-right: 10px;
    border-radius: 50%;
    background: var(--paper);
    vertical-align: 1px;
  }
  .contact {
    position: absolute;
    left: 492px; top: 355px;
    color: var(--paper);
  }
  .contact__name {
    font-weight: 700;
    font-size: 32px;
    margin-bottom: 10px;
  }
  .contact__line {
    display: flex;
    align-items: center;
    font-size: 26px;
    height: 36px;
  }
  .contact__icon {
    width: 28px; height: 28px;
    margin-right: 10px;
    fill: var(--paper);
  }
  .contact__line strong { font-weight: 700; }
</style>
</head>
<body>
  <section class="card card--front">
    <div class="mascot" role="img" aria-label="Cartoon Kordo Bolt mascot flexing its arms"></div>
    <p class="tagline">The Classic Kordo Bolt Products</p>
    <div class="wordmark">Bramble Gear</div>
  </section>

  <section class="card card--back">
    <div class="wordmark">Bramble Gear</div>
    <ul class="services">
      <li>Canvas Seat Covers</li>
      <li>Hi-Vis Flags</li>
      <li>Canvas or PVC designs by request</li>
    </ul>
    <div class="contact">
      <p class="contact__name">Danielle Rowbeck</p>
      <p class="contact__line">
        <svg class="contact__icon" viewBox="0 0 24 24" aria-hidden="true"><path d="M6.6 10.8a15.1 15.1 0 0 0 6.6 6.6l2.2-2.2c.3-.3.7-.4 1-.2 1.1.4 2.3.6 3.6.6.6 0 1 .4 1 1V20c0 .6-.4 1-1 1A17 17 0 0 1 3 4c0-.6.4-1 1-1h3.5c.6 0 1 .4 1 1 0 1.3.2 2.5.6 3.6.1.3 0 .7-.2 1z"/></svg>
        02 49315728
      </p>
      <p class="contact__line">
        <svg class="contact__icon" viewBox="0 0 24 24" aria-hidden="true"><path d="M2 5h20v14H2z M4 7v.4l8 5.6 8-5.6V7z M4 9.8V17h16V9.8l-8 5.6z" fill-rule="evenodd"/></svg>
        admin@bramblegear.com.au
      </p>
      <p class="contact__line">
        <svg class="contact__icon" viewBox="0 0 24 24" aria-hidden="true"><path d="M12 2a10 10 0 1 0 0 20 10 10 0 0 0 0-20zm6.9 6h-3a15 15 0 0 0-1.4-3.9A8 8 0 0 1 18.9 8zM12 4c.8 1.2 1.5 2.5 1.9 4h-3.8c.4-1.5 1.1-2.8 1.9-4zM4.3 14a8 8 0 0 1 0-4h3.4a16 16 0 0 0 0 4zm.8 2h3a15 15 0 0 0 1.4 3.9A8 8 0 0 1 5.1 16zm3-8h-3a8 8 0 0 1 4.3-3.9C8.8 5.3 8.4 6.6 8.1 8zM12 20c-.8-1.2-1.5-2.5-1.9-4h3.8c-.4 1.5-1.1 2.8-1.9 4zm2.3-6H9.7a14 14 0 0 1 0-4h4.6a14 14 0 0 1 0 4zm.3 5.9c.6-1.2 1.1-2.5 1.4-3.9h3a8 8 0 0 1-4.4 3.9zm1.7-5.9a16 16 0 0 0 0-4h3.4a8 8 0 0 1 0 4z"/></svg>
        <span>www.<strong>bramblegear</strong>.com.au</span>
      </p>
    </div>
  </section>
</body>
</html>
```